Name card for fertilizer industry

We 1. produce liquid fertilizer 2. gardening supply 3. Import&Export gardening related product.
I want the name card double-sided(Chinese & English version)
detail has chinese charactor for name and address.
Updates
Target Market(s)
Farmers
Industry/Entity Type
Industry
Contact Information for Business Card
Name: Martin Lo (邱偉達)
TEL: +886-47-615204
FAX:+886-47-640173
MOBILE: +886-952-184-603
ADDRESS: No.58, Taoyuan Rd, Beiming Township, Lanping County , TAIWAN(R.O.C) 蘭平縣北明鎮桃源路58號
Look and feel
Each slider illustrates characteristics of the customer's brand and the style your logo design should communicate.

```html
<!DOCTYPE html>
<html lang="zh-Hant">
<head>
<meta charset="utf-8">
<title>禾旺液肥 – Name Card</title>
<link rel="stylesheet" href="https://fonts.googleapis.com/css2?family=Didact+Gothic&family=Noto+Sans+TC:wght@300;400&display=swap">
<style>
  :root {
    --stage: #e9e9e7;
    --card: #ffffff;
    --ink: #3a2e2b;
    --text: #6d6d6d;
    --green: #5bb536;
    --shadow: rgba(0, 0, 0, 0.12);
  }
  * { box-sizing: border-box; margin: 0; padding: 0; }
  html, body { width: 1200px; height: 900px; overflow: hidden; }
  body {
    background: var(--stage);
    font-family: "Didact Gothic", "Noto Sans TC", sans-serif;
    color: var(--text);
    position: relative;
  }
  .card {
    position: absolute;
    left: 250px;
    width: 700px;
    height: 400px;
    background: var(--card);
    box-shadow: 0 6px 18px var(--shadow);
  }
  .card--back { top: 40px; }
  .card--front { top: 460px; }

  .wordmark {
    display: flex;
    align-items: center;
    gap: 14px;
    font-family: "Noto Sans TC", sans-serif;
    font-weight: 300;
    color: var(--ink);
    letter-spacing: 0.12em;
  }
  .wordmark__dot { border-radius: 50%; background: var(--green); flex: none; }

  .card--back .wordmark {
    position: absolute; left: 0; right: 0; top: 0; bottom: 0;
    justify-content: center; font-size: 50px;
  }
  .card--back .wordmark__dot { width: 26px; height: 26px; }

  .card--front .brand-disc {
    position: absolute; left: 40px; top: 40px;
    width: 170px; height: 170px; border-radius: 50%;
    background: var(--green);
  }
  .card--front .wordmark {
    position: absolute; left: 310px; top: 62px; font-size: 52px;
  }
  .card--front .wordmark__dot { display: none; }

  .details { position: absolute; left: 310px; top: 160px; width: 370px; }
  .person__name {
    font-size: 15px; letter-spacing: 0.28em; text-transform: uppercase; color: var(--text);
  }
  .person__name-zh {
    font-family: "Noto Sans TC", sans-serif; font-weight: 400; letter-spacing: 0.2em; margin-left: 10px;
  }
  .person__role { font-size: 13px; color: var(--green); letter-spacing: 0.15em; margin-top: 4px; }

  .contact { list-style: none; margin-top: 18px; }
  .contact li {
    display: flex; align-items: flex-start; gap: 10px;
    font-size: 12.5px; line-height: 1.45; letter-spacing: 0.08em; margin-bottom: 6px;
  }
  .contact svg { flex: none; width: 13px; height: 13px; margin-top: 2px; }
  .contact .zh { font-family: "Noto Sans TC", sans-serif; font-weight: 300; }
</style>
</head>
<body>

<section class="card card--back" aria-label="Card back">
  <div class="wordmark">禾旺液肥<span class="wordmark__dot"></span></div>
</section>

<section class="card card--front" aria-label="Card front">
  <span class="brand-disc"></span>
  <div class="wordmark">禾旺液肥<span class="wordmark__dot"></span></div>

  <div class="details">
    <p class="person__name">Martin Lo<span class="person__name-zh">邱偉達</span></p>
    <p class="person__role">CEO</p>

    <ul class="contact">
      <li>
        <svg viewBox="0 0 12 12"><path d="M6 0.5a4 4 0 0 1 4 4c0 3-4 7-4 7s-4-4-4-7a4 4 0 0 1 4-4z" fill="var(--green)"/><circle cx="6" cy="4.5" r="1.5" fill="#fff"/></svg>
        <span>No.58, Taoyuan Rd, Beiming Township,<br>Lanping County, Taiwan (R.O.C)<br><span class="zh">蘭平縣北明鎮桃源路58號</span></span>
      </li>
      <li>
        <svg viewBox="0 0 12 12"><path d="M2.5 1h2l1 3-1.5 1a7 7 0 0 0 3 3l1-1.5 3 1v2a1 1 0 0 1-1 1A9.5 9.5 0 0 1 1.5 2a1 1 0 0 1 1-1z" fill="var(--green)"/></svg>
        <span>+886-47-615204</span>
      </li>
      <li>
        <svg viewBox="0 0 12 12"><rect x="3" y="0.5" width="6" height="11" rx="1.2" fill="var(--green)"/><rect x="4" y="2" width="4" height="7" fill="#fff"/></svg>
        <span>+886-952-184-603</span>
      </li>
      <li>
        <svg viewBox="0 0 12 12"><rect x="0.5" y="2" width="11" height="8" rx="1" fill="var(--green)"/><path d="M1 2.5l5 4 5-4" fill="none" stroke="#fff" stroke-width="1"/></svg>
        <span>martin.lo@hewang-agri.tw</span>
      </li>
      <li>
        <svg viewBox="0 0 12 12"><circle cx="6" cy="6" r="5.2" fill="none" stroke="var(--green)" stroke-width="1.4"/><path d="M0.8 6h10.4M6 0.8c-2.6 3-2.6 7.4 0 10.4M6 0.8c2.6 3 2.6 7.4 0 10.4" fill="none" stroke="var(--green)" stroke-width="1"/></svg>
        <span>www.hewang-agri.tw</span>
      </li>
    </ul>
  </div>
</section>

</body>
</html>
```